Personal Finance e-commerce website needs a simple budget design

Hello! I am starting to sell downloadable and printable budget planners, as shown in the attached file, for people to plan ahead on their personal finances. <br/><br/>I want to see a one-page design with similar columns (for example, "Expenses, Budget, and Actual"). I would also like to see the basic formula ("Net Income = Gross income - Total Expenses") somewhere on the design. Finally, I want the design to remain mostly minimalistic and simple for the average person to plan their personal monthly budgets.<br/><br/>However, other than that, the overall design, layout, and colors will be at the graphic designer's choice. If you have any questions for me, please let me know. Thank you for your time!

Industry/Entity Type

Financial Planning

Colors

Designer to choose colors to be used in the design.

Requirements
Must have
• I want to see a one-page design with similar columns (for example, "Expenses, Budget, and Actual").
• I want the design to remain mostly minimalistic and simple for the average person to plan their personal monthly budgets.
Nice to have
• I would also like to see the basic formula ("Net Income = Gross income - Total Expenses") somewhere on the design.

```html
<!DOCTYPE html>
<html lang="en">
<head>
<meta charset="utf-8">
<title>Basic Monthly Budget</title>
<link rel="stylesheet" href="https://fonts.googleapis.com/css2?family=Source+Sans+3:wght@400;600&display=swap">
<style>
  :root {
    --red: #b0080e;
    --green: #7acc00;
    --navy: #3e4078;
    --ink: #111111;
    --muted: #8a8a8a;
    --soft-muted: #a9a9a9;
    --mint: #d3fcc6;
    --mint-light: #e8fce2;
    --row-red: rgba(176, 8, 14, 0.48);
    --row-green: rgba(122, 204, 0, 0.45);
    --row-navy: rgba(62, 64, 120, 0.48);
    --row-navy-faint: rgba(62, 64, 120, 0.15);
    --row-tan: #d6c9a5;
  }
  * { box-sizing: border-box; margin: 0; padding: 0; }
  html, body { width: 928px; height: 1200px; overflow: hidden; background: #fff; }
  body { font-family: "Source Sans 3", sans-serif; color: var(--ink); }
  .sheet { position: relative; width: 928px; height: 1200px; overflow: hidden; background: #fff; }
  .backdrop { position: absolute; inset: 0; }
  .abs { position: absolute; }

  .brand {
    left: 65px; top: 55px; width: 134px; height: 102px;
    border: 1.5px solid var(--ink); border-radius: 50%;
    display: flex; flex-direction: column; align-items: center; justify-content: center;
    background: #fff;
  }
  .brand-mark { font-size: 27px; line-height: 1; }
  .brand-name { font-size: 15px; margin-top: 6px; letter-spacing: 0.3px; }

  .period-line { left: 584px; top: 92px; width: 300px; height: 3px; background: var(--green); }
  .period-label { top: 107px; font-size: 18px; letter-spacing: 0.5px; }
  .period-month { left: 632px; }
  .period-year { left: 782px; }

  .title { left: 0; width: 928px; top: 164px; text-align: center; font-size: 37px; font-weight: 400; letter-spacing: 0.3px; }
  .title-rule { left: 45px; top: 214px; width: 839px; height: 3px; background: var(--red); }

  .col-head { color: #fff; display: flex; align-items: center; justify-content: center; text-align: center; letter-spacing: 0.5px; }
  .head-expenses { left: 45px; top: 239px; width: 839px; height: 90px; background: var(--red); justify-content: flex-start; padding-left: 48px; font-size: 32px; line-height: 1.18; text-align: left; align-items: center; }
  .head-budget { left: 306px; top: 253px; width: 578px; height: 91px; background: var(--green); justify-content: flex-start; padding-left: 54px; font-size: 32px; }
  .head-actual { left: 598px; top: 264px; width: 286px; height: 90px; background: var(--navy); font-size: 32px; }

  .col-hint { font-size: 13px; color: var(--muted); text-align: center; line-height: 1.35; }
  .hint-expenses { left: 85px; width: 160px; top: 341px; }
  .hint-budget { left: 374px; width: 160px; top: 355px; }
  .hint-actual { left: 690px; width: 160px; top: 365px; }

  .row { height: 73px; }
  .row-tab { left: 4px; width: 41px; background: var(--row-tan); }
  .row-expense { left: 45px; width: 254px; background: var(--row-red); }
  .row-budget { left: 312px; width: 286px; background: var(--row-green); }
  .row-actual { left: 617px; width: 267px; background: var(--row-navy); }
  .row-actual-tail { left: 884px; width: 43px; background: var(--row-navy-faint); }

  .formula-head { top: 1011px; height: 45px; color: #fff; font-size: 32px; display: flex; align-items: center; justify-content: center; letter-spacing: 0.8px; }
  .formula-body { top: 1056px; height: 70px; background: rgba(255,255,255,0.9); color: var(--soft-muted); font-size: 19px; letter-spacing: 0.8px; line-height: 1.2; display: flex; align-items: center; justify-content: center; text-align: center; }
  .f-net { left: 45px; width: 224px; }
  .f-gross { left: 314px; width: 224px; }
  .f-total { left: 584px; width: 300px; }
  .formula-head.f-net, .formula-head.f-gross { background: var(--navy); }
  .formula-head.f-total { background: var(--green); }
  .op-equals { left: 282px; top: 1028px; width: 22px; height: 12px; border-top: 3px solid var(--green); border-bottom: 3px solid var(--green); }
  .op-minus { left: 552px; top: 1034px; width: 19px; height: 4px; background: var(--red); }

  .web { left: 0; width: 928px; top: 1146px; text-align: center; font-size: 19px; letter-spacing: 0.6px; }
</style>
</head>
<body>
<main class="sheet">
  <svg class="backdrop" width="928" height="1200" viewBox="0 0 928 1200" aria-hidden="true">
    <polygon points="0,162 256,600 465,682 605,1012 561,1200 0,1200" fill="var(--mint)"/>
    <polygon points="330,1200 476,847 928,720 928,1200" fill="var(--mint-light)"/>
  </svg>

  <div class="abs brand"><span class="brand-mark">Logo</span><span class="brand-name">Company name</span></div>

  <div class="abs period-line"></div>
  <span class="abs period-label period-month">Month</span>
  <span class="abs period-label period-year">Year</span>

  <h1 class="abs title">BASIC MONTHYL BUDGET</h1>
  <div class="abs title-rule"></div>

  <div class="abs col-head head-expenses">Expenses<br>(category)</div>
  <div class="abs col-head head-budget">Budget (USD)</div>
  <div class="abs col-head head-actual">Actual (USD)</div>

  <p class="abs col-hint hint-expenses">Custom category</p>
  <p class="abs col-hint hint-budget">What you plan to<br>spend</p>
  <p class="abs col-hint hint-actual">What you actually<br>spent</p>

  <div class="abs row row-tab" style="top:412px"></div><div class="abs row row-expense" style="top:412px"></div><div class="abs row row-budget" style="top:412px"></div><div class="abs row row-actual" style="top:410px"></div><div class="abs row row-actual-tail" style="top:410px"></div>
  <div class="abs row row-tab" style="top:496px"></div><div class="abs row row-expense" style="top:496px"></div><div class="abs row row-budget" style="top:496px"></div><div class="abs row row-actual" style="top:494px"></div><div class="abs row row-actual-tail" style="top:494px"></div>
  <div class="abs row row-tab" style="top:578px"></div><div class="abs row row-expense" style="top:578px"></div><div class="abs row row-budget" style="top:578px"></div><div class="abs row row-actual" style="top:576px"></div><div class="abs row row-actual-tail" style="top:576px"></div>
  <div class="abs row row-tab" style="top:662px"></div><div class="abs row row-expense" style="top:662px"></div><div class="abs row row-budget" style="top:662px"></div><div class="abs row row-actual" style="top:660px"></div><div class="abs row row-actual-tail" style="top:660px"></div>
  <div class="abs row row-tab" style="top:746px"></div><div class="abs row row-expense" style="top:746px"></div><div class="abs row row-budget" style="top:746px"></div><div class="abs row row-actual" style="top:744px"></div><div class="abs row row-actual-tail" style="top:744px"></div>
  <div class="abs row row-tab" style="top:829px"></div><div class="abs row row-expense" style="top:829px"></div><div class="abs row row-budget" style="top:829px"></div><div class="abs row row-actual" style="top:827px"></div><div class="abs row row-actual-tail" style="top:827px"></div>
  <div class="abs row row-tab" style="top:913px"></div><div class="abs row row-expense" style="top:913px"></div><div class="abs row row-budget" style="top:913px"></div><div class="abs row row-actual" style="top:910px"></div><div class="abs row row-actual-tail" style="top:910px"></div>

  <div class="abs formula-head f-net">Net Income</div>
  <div class="abs op-equals"></div>
  <div class="abs formula-head f-gross">Gross Income</div>
  <div class="abs op-minus"></div>
  <div class="abs formula-head f-total">Total Expenses</div>

  <div class="abs formula-body f-net">How much money<br>you kept</div>
  <div class="abs formula-body f-gross">How much money<br>you earned</div>
  <div class="abs formula-body f-total">Actual Expenses</div>

  <p class="abs web">www.Web page.com</p>
</main>
</body>
</html>
```